PineCrest Gate
business card and stationary?
I need double sided standard sized Business Card [3.5" x 2"]
use something easy to read and professional
Professional
Colin Dawlish
Owner
24681 K St
PO Box 517264
Omaha, NE 68247
Colin@PineCrestGate.com
PineCrestGate.com
We Promise Satisfaction!
Custom garage doors built for you!
Longer lasting Torsion springs!
HoistWell Openers
Brookvale and Garvey Doors

```html
<!DOCTYPE html>
<html lang="en">
<head>
<meta charset="utf-8">
<title>PineCrest Gate Stationery</title>
<link href="https://fonts.googleapis.com/css2?family=Open+Sans:wght@400;600;700&display=swap" rel="stylesheet">
<style>
:root{
  --bg:#ece9e4;
  --paper:#ffffff;
  --teal:#1f8aa6;
  --teal-dark:#15677d;
  --navy:#1e3e5c;
  --grey:#8d9297;
  --grey-light:#c9ccd0;
  --ink:#3a4550;
  --dark-card:#1d232a;
  --faint:#e6eef3;
}
*{box-sizing:border-box;margin:0;padding:0}
html,body{width:1200px;height:317px;overflow:hidden;background:var(--bg);font-family:"Open Sans",Arial,sans-serif;color:var(--ink)}
.board{position:relative;width:1200px;height:317px}
.piece{position:absolute;background:var(--paper);box-shadow:0 1px 4px rgba(0,0,0,.25);overflow:hidden}
.caption{position:absolute;font-size:5px;color:#6c6c6c;white-space:nowrap}
.brand{display:flex;align-items:center;gap:3px;font-weight:700;color:var(--navy);white-space:nowrap}
.brand .dot{border-radius:50%;background:var(--teal);flex:none}
.brand.light{color:#fff}
.section-title{position:absolute;left:19px;top:96px;font-size:5px;color:#6c6c6c}

/* business cards */
.card{width:77px;height:44px}
.card .brand{position:absolute;left:6px;top:8px;font-size:6px}
.card .brand .dot{width:7px;height:7px}
.card .details{position:absolute;left:6px;top:20px;font-size:3px;line-height:4px}
.card .band{position:absolute;left:0;right:0;bottom:0;height:4px;background:var(--teal)}
.card.dark{background:var(--dark-card)}
.card.dark .details{color:#d5dbe0}
.card .mark{position:absolute;left:26px;top:8px;width:26px;height:26px;border-radius:50%;background:var(--teal)}

/* letterheads */
.letterhead{width:210px;height:298px;top:12px}
.letterhead .brand{position:absolute;left:14px;top:16px;font-size:10px}
.letterhead .brand .dot{width:11px;height:11px}
.letterhead .address{position:absolute;left:28px;top:30px;font-size:3.5px;color:var(--grey)}
.letterhead .rule{position:absolute;right:14px;top:24px;width:70px;height:1px;background:var(--grey-light)}
.letterhead .watermark{position:absolute;left:72px;top:120px;width:66px;height:66px;border-radius:50%;background:var(--faint)}
.letterhead .foot-grey{position:absolute;left:0;right:0;bottom:0;height:10px;background:var(--grey-light)}
.letterhead .foot-teal{position:absolute;right:0;bottom:0;width:110px;height:10px;background:var(--teal);clip-path:polygon(8% 0,100% 0,100% 100%,0 100%)}
.letterhead .foot-text{position:absolute;left:14px;bottom:2px;font-size:3.5px;color:#fff}

/* envelopes */
.envelope{width:211px;height:112px;left:665px}
.envelope .brand{position:absolute;left:10px;top:12px;font-size:8px}
.envelope .brand .dot{width:9px;height:9px}
.envelope .address{position:absolute;left:22px;top:24px;font-size:3.5px;color:var(--grey)}
.envelope .watermark{position:absolute;right:30px;top:28px;width:50px;height:50px;border-radius:50%;background:var(--faint)}
.envelope .foot{position:absolute;right:0;bottom:0;width:120px;height:8px;background:var(--teal);clip-path:polygon(6% 0,100% 0,100% 100%,0 100%)}
.envelope .foot-grey{position:absolute;left:0;bottom:0;width:96px;height:8px;background:var(--grey-light)}

/* envelope backs */
.env-back{position:absolute;left:888px;width:288px}
</style>
</head>
<body>
<main class="board">

  <!-- business cards -->
  <div class="piece card" style="left:19px;top:106px">
    <div class="brand"><span class="dot"></span>PineCrest Gate</div>
    <div class="details">Colin Dawlish, Owner<br>24681 K St, Omaha, NE 68247<br>Colin@PineCrestGate.com</div>
    <div class="band"></div>
  </div>
  <div class="piece card dark" style="left:96px;top:106px">
    <div class="brand light"><span class="dot"></span>PineCrest Gate</div>
    <div class="details">We Promise Satisfaction!<br>HoistWell Openers<br>PineCrestGate.com</div>
    <div class="band"></div>
  </div>
  <div class="caption" style="left:19px;top:152px">Card Front</div>
  <div class="caption" style="left:96px;top:152px">Card Back</div>

  <div class="piece card" style="left:19px;top:160px">
    <div class="mark"></div>
    <div class="band"></div>
  </div>
  <div class="piece card dark" style="left:96px;top:160px">
    <div class="brand light"><span class="dot"></span>PineCrest Gate</div>
    <div class="details">Custom garage doors built for you!<br>Brookvale and Garvey Doors</div>
    <div class="band"></div>
  </div>
  <div class="caption" style="left:19px;top:206px">Card Front</div>
  <div class="caption" style="left:96px;top:206px">Card Back</div>
  <div class="caption" style="left:19px;top:98px">Business Card Design</div>

  <!-- letterheads -->
  <section class="piece letterhead" style="left:211px">
    <div class="brand"><span class="dot"></span>PineCrest Gate</div>
    <div class="address">24681 K St · Omaha, NE 68247</div>
    <div class="rule"></div>
    <div class="watermark"></div>
    <div class="foot-grey"></div><div class="foot-teal"></div>
    <div class="foot-text">PineCrestGate.com</div>
  </section>
  <div class="caption" style="left:290px;top:311px">Letterhead Design</div>

  <section class="piece letterhead" style="left:439px">
    <div class="brand"><span class="dot"></span>PineCrest Gate</div>
    <div class="address">PO Box 517264 · Omaha, NE 68247</div>
    <div class="rule"></div>
    <div class="watermark"></div>
    <div class="foot-grey"></div><div class="foot-teal"></div>
    <div class="foot-text">Colin@PineCrestGate.com</div>
  </section>
  <div class="caption" style="left:518px;top:311px">Letterhead Design</div>

  <!-- envelopes -->
  <section class="piece envelope" style="top:29px">
    <div class="brand"><span class="dot"></span>PineCrest Gate</div>
    <div class="address">24681 K St · Omaha, NE 68247</div>
    <div class="watermark"></div>
    <div class="foot-grey"></div><div class="foot"></div>
  </section>
  <div class="caption" style="left:745px;top:168px">Envelope Design</div>

  <section class="piece envelope" style="top:187px">
    <div class="brand"><span class="dot"></span>PineCrest Gate</div>
    <div class="address">PO Box 517264 · Omaha, NE 68247</div>
    <div class="watermark"></div>
    <div class="foot-grey"></div><div class="foot"></div>
  </section>
  <div class="caption" style="left:745px;top:304px">Envelope Design</div>

  <!-- envelope backs -->
  <svg class="env-back" style="top:20px" width="288" height="280" viewBox="0 0 288 280" aria-hidden="true">
    <rect x="0" y="0" width="288" height="86" fill="var(--teal)"/>
    <rect x="0" y="0" width="288" height="12" fill="var(--teal-dark)"/>
    <rect x="0" y="92" width="288" height="90" fill="var(--grey)"/>
    <rect x="0" y="92" width="288" height="14" fill="#6f757a"/>
    <rect x="0" y="188" width="288" height="88" fill="var(--paper)"/>
    <polygon points="0,188 144,246 288,188" fill="#f2f4f6" stroke="var(--grey-light)" stroke-width="1"/>
    <line x1="0" y1="276" x2="130" y2="232" stroke="var(--grey-light)"/>
    <line x1="288" y1="276" x2="158" y2="232" stroke="var(--grey-light)"/>
  </svg>
  <div class="caption" style="left:1000px;top:300px">Envelope Back Design</div>

</main>
</body>
</html>
```